Medical Waste Company with Logo

Need a business card design that targets office managers in the medical community. This card will be the front line for our sales team to market our services to the community. We would like to have email, phone number, website. Please use the logo attached to create a design that we would be proud of.

Target Market(s)

Medical Clients

Industry/Entity Type

Medical Supply

Contact Information for Business Card

Please use logo attached

Colors

Designer to choose colors to be used in the design.

Requirements
Must have
• Our logo (see attached file)
Nice to have
• Maybe a pop of some sort, raised..?

```html
<!DOCTYPE html>
<html lang="en">
<head>
<meta charset="UTF-8">
<title>Northpeak Clinical Disposal – Business Card</title>
<link rel="stylesheet" href="https://fonts.googleapis.com/css2?family=Montserrat:wght@400;600;700&display=swap">
<style>
  :root {
    --page-bg: #e9ecef;
    --card-bg: #ffffff;
    --brand-blue: #1c5a99;
    --text-grey: #808080;
    --name-grey: #7a7a7a;
  }
  * { box-sizing: border-box; margin: 0; padding: 0; }
  html, body {
    width: 1200px;
    height: 1200px;
    overflow: hidden;
    background: var(--page-bg);
    font-family: "Montserrat", Arial, sans-serif;
  }
  .business-card {
    position: absolute;
    left: 100px;
    top: 314px;
    width: 1000px;
    height: 572px;
    background: var(--card-bg);
    box-shadow: 0 10px 30px rgba(0,0,0,0.12);
  }
  .brand-lockup {
    position: absolute;
    left: 70px;
    top: 250px;
    display: flex;
    align-items: center;
    gap: 16px;
  }
  .brand-square {
    width: 34px;
    height: 34px;
    background: var(--brand-blue);
  }
  .brand-name {
    color: var(--brand-blue);
    font-weight: 700;
    font-size: 27px;
    line-height: 1.15;
    letter-spacing: 0.5px;
    text-transform: uppercase;
  }
  .name-marker {
    position: absolute;
    left: 540px;
    top: 150px;
    width: 4px;
    height: 34px;
    background: var(--brand-blue);
  }
  .divider {
    position: absolute;
    left: 540px;
    top: 222px;
    width: 2px;
    height: 180px;
    background: var(--brand-blue);
  }
  .person {
    position: absolute;
    left: 570px;
    top: 140px;
  }
  .person-name {
    color: var(--name-grey);
    font-weight: 700;
    font-size: 30px;
    line-height: 1.1;
  }
  .person-title {
    color: var(--text-grey);
    font-size: 19px;
    font-weight: 400;
  }
  .contact-list {
    position: absolute;
    left: 570px;
    top: 226px;
    list-style: none;
  }
  .contact-item {
    display: flex;
    align-items: center;
    gap: 14px;
    height: 40px;
    color: var(--text-grey);
    font-size: 21px;
  }
  .contact-icon {
    width: 24px;
    height: 24px;
    flex: none;
    fill: var(--brand-blue);
  }
</style>
</head>
<body>
  <div class="business-card">
    <div class="brand-lockup">
      <div class="brand-square"></div>
      <div class="brand-name">Northpeak Clinical<br>Disposal</div>
    </div>

    <div class="name-marker"></div>
    <div class="person">
      <p class="person-name">Daniel Hart</p>
      <p class="person-title">Director</p>
    </div>

    <div class="divider"></div>
    <ul class="contact-list">
      <li class="contact-item">
        <svg class="contact-icon" viewBox="0 0 24 24" aria-hidden="true"><path d="M12 2a7 7 0 0 0-7 7c0 5 7 13 7 13s7-8 7-13a7 7 0 0 0-7-7zm0 9.5A2.5 2.5 0 1 1 12 6.5a2.5 2.5 0 0 1 0 5z"/></svg>
        <span>Address 1234 street city</span>
      </li>
      <li class="contact-item">
        <svg class="contact-icon" viewBox="0 0 24 24" aria-hidden="true"><path d="M6.6 10.8a15.1 15.1 0 0 0 6.6 6.6l2.2-2.2a1 1 0 0 1 1-.25 11.4 11.4 0 0 0 3.6.57 1 1 0 0 1 1 1V20a1 1 0 0 1-1 1A17 17 0 0 1 3 4a1 1 0 0 1 1-1h3.5a1 1 0 0 1 1 1c0 1.25.2 2.45.57 3.57a1 1 0 0 1-.25 1z"/></svg>
        <span>+00 000 0000 00</span>
      </li>
      <li class="contact-item">
        <svg class="contact-icon" viewBox="0 0 24 24" aria-hidden="true"><path d="M2 5h20v14H2z M3.5 6.5 12 13l8.5-6.5" fill="none" stroke="#1c5a99" stroke-width="2"/><path d="M2 5h20l-10 8z"/></svg>
        <span>yourmail@mail.com</span>
      </li>
      <li class="contact-item">
        <svg class="contact-icon" viewBox="0 0 24 24" aria-hidden="true"><circle cx="12" cy="12" r="10"/><path d="M2 12h20M12 2c3 3 3 17 0 20M12 2c-3 3-3 17 0 20" fill="none" stroke="#fff" stroke-width="1.4"/></svg>
        <span>www.yourweb.com</span>
      </li>
    </ul>
  </div>
</body>
</html>
```